BRIGHTWATER BUILDERS, INC. ELECTRICAL SERVICE

We need a tri-fold pamphlet design for electrical service based in NW Arkansas. We offer Commercial and Industrial Electrical Services including: Infrared imaging, Data Cable Testing, Fiber Optics Testing & Repair, Utility Locates, Preventative Maintenance, Lighting Inspections, Electrical Equipment Cleaning, Automatic Transfer Switch Testing, LED Upgrades with Energy Savings Report.

```html
<!DOCTYPE html>
<html lang="en">
<head>
<meta charset="utf-8">
<title>Brightwater Builders – Electrical Service Tri-fold</title>
<link rel="stylesheet" href="https://fonts.googleapis.com/css2?family=Open+Sans:wght@300;400;600;700&family=Montserrat:wght@300;400;800&family=Oswald:wght@600&display=swap">
<style>
  :root {
    --stage: #3b3b3d;
    --blue: #0b3aa8;
    --ink: #2b2b2d;
    --body: #555558;
    --paper: #ffffff;
    --panel-grey: #ececed;
    --dark: #1d1d1f;
    --tag-grey: #4a4a4c;
  }
  * { box-sizing: border-box; margin: 0; padding: 0; }
  html, body { width: 1200px; height: 800px; overflow: hidden; background: var(--stage); }
  body { font-family: "Open Sans", Arial, sans-serif; color: var(--body); }

  .brochure {
    position: absolute; left: 45px; top: 40px; width: 1110px; height: 720px;
    background: var(--paper); box-shadow: 0 18px 40px rgba(0,0,0,.45); overflow: hidden;
  }
  .brochure-shapes { position: absolute; inset: 0; }
  .panel { position: absolute; top: 0; width: 370px; height: 720px; }
  .panel-about { left: 0; }
  .panel-contact { left: 370px; }
  .panel-cover { left: 740px; }

  .section-title {
    font-family: "Montserrat", sans-serif; font-weight: 300; font-size: 24px;
    color: var(--ink); letter-spacing: .5px;
  }
  .section-title strong { font-weight: 800; color: var(--blue); }
  .title-rule { width: 18px; height: 3px; background: var(--blue); margin: 8px 0 12px; }

  .panel-about .inner { position: absolute; left: 48px; top: 62px; width: 285px; }
  .copy { font-size: 11.5px; line-height: 1.55; color: var(--body); }
  .pitch { margin: 16px 0 10px; font-family: "Montserrat", sans-serif; line-height: 1.1; }
  .pitch .light { display: block; font-weight: 300; font-size: 20px; color: var(--ink); }
  .pitch .bold { display: block; font-weight: 800; font-size: 19px; color: var(--blue); letter-spacing: .4px; }

  .service-list { list-style: none; font-size: 11px; line-height: 1.45; color: var(--body); }
  .service-list li { position: relative; padding-left: 16px; }
  .service-list li::before {
    content: ""; position: absolute; left: 2px; top: 3px; width: 4px; height: 8px;
    border: solid var(--blue); border-width: 0 2px 2px 0; transform: rotate(45deg);
  }

  .panel-contact .inner { position: absolute; left: 0; top: 215px; width: 370px; text-align: center; }
  .panel-contact .title-rule { margin: 8px auto 16px; }
  .office { margin-bottom: 26px; font-size: 11.5px; line-height: 1.55; color: var(--ink); }
  .office-name {
    font-family: "Montserrat", sans-serif; font-weight: 800; font-size: 13px;
    color: var(--blue); letter-spacing: .5px; margin-bottom: 4px;
  }
  .office .label { color: var(--blue); font-weight: 700; }
  .icon { width: 10px; height: 10px; vertical-align: -1px; margin-right: 4px; fill: var(--blue); }

  .site-link {
    position: absolute; left: 0; width: 370px; text-align: center;
    font-family: "Montserrat", sans-serif; font-size: 14px; letter-spacing: 3px; color: #fff;
  }
  .panel-contact .site-link { top: 650px; }
  .globe { position: absolute; left: 174px; top: 615px; width: 22px; height: 22px; }

  .wordmark {
    position: absolute; left: 70px; top: 44px; display: flex; align-items: center; gap: 10px;
    font-family: "Montserrat", sans-serif; font-weight: 800; font-size: 19px;
    color: var(--blue); letter-spacing: .5px; line-height: 1.1;
  }
  .wordmark-dot { width: 16px; height: 16px; background: var(--blue); flex: none; }

  .tag-box {
    position: absolute; left: 120px; top: 440px; width: 230px; height: 110px;
    background: var(--tag-grey); transform: rotate(-16deg);
    display: flex; align-items: center; justify-content: center;
    font-family: "Oswald", sans-serif; font-weight: 600; font-size: 25px;
    line-height: 1.1; color: #fff; text-transform: uppercase; text-align: left;
    box-shadow: 0 6px 14px rgba(0,0,0,.3);
  }
  .panel-cover .site-link { top: 640px; transform: rotate(-10deg); font-size: 13px; }
</style>
</head>
<body>
<main class="brochure">
  <svg class="brochure-shapes" width="1110" height="720" viewBox="0 0 1110 720">
    <defs>
      <linearGradient id="factoryTone" x1="0" y1="0" x2="1" y2="1">
        <stop offset="0" stop-color="#e6e8ec"/><stop offset=".6" stop-color="#c7d0db"/><stop offset="1" stop-color="#8fa3bb"/>
      </linearGradient>
      <linearGradient id="robotTone" x1="0" y1="0" x2="1" y2="1">
        <stop offset="0" stop-color="#1f4fb8"/><stop offset=".5" stop-color="#c9a52a"/><stop offset="1" stop-color="#2d5fc4"/>
      </linearGradient>
      <linearGradient id="panelTone" x1="0" y1="0" x2="1" y2="1">
        <stop offset="0" stop-color="#d8d6d2"/><stop offset=".5" stop-color="#c9b98a"/><stop offset="1" stop-color="#9b9ea3"/>
      </linearGradient>
    </defs>

    <!-- about panel -->
    <path class="photo-factory" d="M0 530 Q200 515 370 490 L370 660 L0 660 Z" fill="url(#factoryTone)" role="img" aria-label="Automated factory line with conveyor belts and robotic arms"/>
    <path class="band-dark" d="M0 665 Q210 650 370 565 L370 720 L0 720 Z" fill="#1d1d1f"/>
    <path class="band-blue" d="M0 690 Q200 680 330 645 L370 630 L370 720 L0 720 Z" fill="#0b3aa8"/>

    <!-- contact panel -->
    <rect x="370" y="0" width="370" height="720" fill="#ececed"/>
    <path class="photo-robots" d="M370 0 H740 V150 Q560 250 370 185 Z" fill="url(#robotTone)" role="img" aria-label="Yellow industrial robot arms in a blue-lit plant"/>
    <path class="band-dark" d="M370 610 Q570 590 740 500 L740 720 L370 720 Z" fill="#1d1d1f"/>

    <!-- cover panel -->
    <path class="photo-electrical" d="M740 120 L1110 150 L1110 720 L740 720 Z" fill="url(#panelTone)" role="img" aria-label="Electrician testing wires in an electrical control panel"/>
    <path class="band-blue" d="M740 580 Q920 545 1110 450 L1110 720 L740 720 Z" fill="#0b3aa8"/>
    <line x1="370" y1="0" x2="370" y2="720" stroke="rgba(0,0,0,.08)"/>
    <line x1="740" y1="0" x2="740" y2="720" stroke="rgba(0,0,0,.08)"/>
  </svg>

  <section class="panel panel-about">
    <div class="inner">
      <h2 class="section-title">ABOUT <strong>US</strong></h2>
      <div class="title-rule"></div>
      <p class="copy">Since 1972, Brightwater has served Northwest Arkansas. Our electrical service team delivers commercial and industrial work that keeps your facility safe, efficient and running.</p>
      <h3 class="pitch">
        <span class="light">SAVING YOU</span>
        <span class="bold">TIME &amp; MONEY WITH</span>
        <span class="light">THE RIGHT PEOPLE,</span>
        <span class="bold">RIGHT EQUIPMENT</span>
        <span class="bold">&amp; RIGHT EXPERIENCE</span>
      </h3>
      <ul class="service-list">
        <li>Infrared Imaging</li>
        <li>Data Cable Testing</li>
        <li>Fiber Optics Testing &amp; Repair</li>
        <li>Utility Locates</li>
        <li>Preventative Maintenance</li>
        <li>Lighting Inspections</li>
        <li>Electrical Equipment Cleaning</li>
        <li>Automatic Transfer Switch Testing</li>
        <li>LED Upgrades with Energy Savings Report</li>
      </ul>
    </div>
  </section>

  <section class="panel panel-contact">
    <div class="inner">
      <h2 class="section-title">CONTACT <strong>US</strong></h2>
      <div class="title-rule"></div>
      <div class="office">
        <p class="office-name">SPRINGDALE</p>
        <p><svg class="icon" viewBox="0 0 10 10"><path d="M5 0a3.5 3.5 0 0 0-3.5 3.5C1.5 6 5 10 5 10s3.5-4 3.5-6.5A3.5 3.5 0 0 0 5 0zm0 5a1.5 1.5 0 1 1 0-3 1.5 1.5 0 0 1 0 3z"/></svg>1480 North Cedar Ridge Road<br>P. O. Box 2290<br>Springdale, AR 72764-2290</p>
        <p><svg class="icon" viewBox="0 0 10 10"><path d="M2 0l2 2.5-1 1.2c.6 1.3 1.6 2.3 2.9 2.9l1.2-1L10 7.6 8.6 10C4 9.6.4 6 0 1.4z"/></svg>(479) 555-0142</p>
        <p><span class="label">Toll-Free:</span> (800) 555-0187</p>
        <p><svg class="icon" viewBox="0 0 10 10"><path d="M2.5 0h5v3h-5zM0 3.5h10v4H8V10H2V7.5H0zm3 3.5v2h4V7z"/></svg>(479) 555-0199</p>
      </div>
      <div class="office">
        <p class="office-name">SPRINGFIELD</p>
        <p><svg class="icon" viewBox="0 0 10 10"><path d="M5 0a3.5 3.5 0 0 0-3.5 3.5C1.5 6 5 10 5 10s3.5-4 3.5-6.5A3.5 3.5 0 0 0 5 0zm0 5a1.5 1.5 0 1 1 0-3 1.5 1.5 0 0 1 0 3z"/></svg>3650 North Birchwood Road<br>Springfield, MO 65802</p>
        <p><svg class="icon" viewBox="0 0 10 10"><path d="M2 0l2 2.5-1 1.2c.6 1.3 1.6 2.3 2.9 2.9l1.2-1L10 7.6 8.6 10C4 9.6.4 6 0 1.4z"/></svg>(417) 555-0163</p>
        <p><span class="label">Toll-Free:</span> (800) 555-0124</p>
        <p><svg class="icon" viewBox="0 0 10 10"><path d="M2.5 0h5v3h-5zM0 3.5h10v4H8V10H2V7.5H0zm3 3.5v2h4V7z"/></svg>(417) 555-0178</p>
      </div>
    </div>
    <svg class="globe" viewBox="0 0 22 22" fill="none" stroke="#fff" stroke-width="1.4">
      <circle cx="11" cy="11" r="9"/><ellipse cx="11" cy="11" rx="4" ry="9"/><line x1="2" y1="11" x2="20" y2="11"/><line x1="4" y1="6" x2="18" y2="6"/><line x1="4" y1="16" x2="18" y2="16"/>
    </svg>
    <p class="site-link">www.brightwater-builders.net</p>
  </section>

  <section class="panel panel-cover">
    <div class="wordmark"><span class="wordmark-dot"></span><span>BRIGHTWATER<br>BUILDERS, INC.</span></div>
    <div class="tag-box">From Concept<br>to Completion</div>
    <p class="site-link">www.brightwater-builders.net</p>
  </section>
</main>
</body>
</html>
```